Medical equipment business looking for professional, unique business card

We need a business card design for a durable medical equipment company. We are small but would like our cards to express that we are much bigger. We focus on braces (back, knee, wrist, etc) but also do crutches, rollators, wheelchairs- basically medical equipment that gets you going and back in Action. Our colors are blue and green and our logo has an arrow and use of a "spine". We'd like to express professionalism while being unique.

Industry/Entity Type

Medical Equipment

Contact Information for Business Card

Professional feel but unique. Memorable.

Font styles to use
Serif
Sans Serif
Other font styles liked:
• verdana

Requirements
Must have
• card holders cell#, business phone#, fax#, email, website address, business address, logo
Nice to have
• use of medical/healthcare related descriptive words, items, look
Should not have
• the wrong colors or cartoon characters.

```html
<!DOCTYPE html>
<html lang="en">
<head>
<meta charset="utf-8">
<title>Stride DME – Business Card</title>
<link href="https://fonts.googleapis.com/css2?family=Source+Sans+3:wght@400;600&display=swap" rel="stylesheet">
<style>
  :root {
    --backdrop: #676767;
    --card-white: #ffffff;
    --card-green: #8dc63f;
    --navy: #1d4f7c;
    --sky: #1a8cc8;
    --ink: #1e1e1e;
  }
  * { margin: 0; padding: 0; box-sizing: border-box; }
  html, body {
    width: 1200px; height: 900px; overflow: hidden;
    background: var(--backdrop);
    font-family: "Source Sans 3", "Verdana", sans-serif;
  }
  .stage { position: relative; width: 1200px; height: 900px; }
  .card {
    position: absolute; top: 200px; width: 310px; height: 502px;
  }
  .card-front {
    left: 265px; background: var(--card-white);
    border-radius: 56px 0 70px 0;
  }
  .card-back {
    left: 641px; background: var(--card-green);
    border-radius: 0 56px 0 70px;
    display: flex; align-items: center; justify-content: center;
  }
  .brand {
    position: absolute; left: 20px; top: 88px;
    display: flex; align-items: center; gap: 10px;
  }
  .brand-dot {
    width: 14px; height: 14px; border-radius: 50%;
    background: var(--card-green);
  }
  .brand-name {
    font-size: 36px; font-weight: 600; color: var(--navy);
    line-height: 1; letter-spacing: 0.3px;
  }
  .back-name {
    font-size: 40px; font-weight: 600; color: var(--navy);
    line-height: 1;
  }
  .holder { position: absolute; left: 16px; top: 235px; }
  .holder-name {
    font-size: 21px; font-weight: 600; color: var(--sky); line-height: 1.1;
  }
  .holder-role {
    font-size: 16px; color: var(--ink); margin-top: 4px; line-height: 1.1;
  }
  .contacts {
    position: absolute; left: 17px; top: 300px; list-style: none;
  }
  .contacts li {
    display: flex; align-items: center; gap: 5px;
    font-size: 13.5px; color: var(--ink); height: 18px;
  }
  .contacts svg { width: 9px; height: 9px; fill: var(--sky); flex: none; }
  .address {
    position: absolute; left: 16px; top: 410px;
    font-size: 13.5px; color: var(--ink); line-height: 18px; font-style: normal;
  }
</style>
</head>
<body>
<div class="stage">
  <section class="card card-front">
    <div class="brand">
      <span class="brand-dot"></span>
      <span class="brand-name">Stride DME</span>
    </div>

    <div class="holder">
      <p class="holder-name">Clara Whitfield</p>
      <p class="holder-role">Marketing</p>
    </div>

    <ul class="contacts">
      <li>
        <svg viewBox="0 0 10 10"><path d="M1 4 Q5 0 9 4 L8 5 L6.5 4 L6.5 3.5 Q5 3 3.5 3.5 L3.5 4 L2 5 Z M2.5 5.5 H7.5 L8.5 9 H1.5 Z"/></svg>
        + 61 400123987
      </li>
      <li>
        <svg viewBox="0 0 10 10"><path d="M3 0 H7 Q8 0 8 1 V9 Q8 10 7 10 H3 Q2 10 2 9 V1 Q2 0 3 0 Z M3 1.5 V7.5 H7 V1.5 Z"/></svg>
        + 61 2 9000 4512
      </li>
      <li>
        <svg viewBox="0 0 10 10"><path d="M2.5 1 H7 V4 H9 V9 H1 V4 H2.5 Z M3.5 2 V4 H6 V2 Z M3 5.5 V7 H7 V5.5 Z"/></svg>
        (402)-66-318
      </li>
      <li>
        <svg viewBox="0 0 10 10"><path d="M0.5 2 H9.5 V8 H0.5 Z M1.3 2.8 L5 5.5 L8.7 2.8 V3.6 L5 6.3 L1.3 3.6 Z" fill-rule="evenodd"/></svg>
        hello@stridedme.com
      </li>
      <li>
        <svg viewBox="0 0 10 10"><circle cx="5" cy="5" r="4.6"/></svg>
        www.stridedme.co
      </li>
    </ul>

    <address class="address">
      Suite 8, Level 2, 14-18 Harbour Lane,<br>
      Sydney, NSW, 2000, Australia
    </address>
  </section>

  <section class="card card-back">
    <span class="back-name">Stride DME</span>
  </section>
</div>
</body>
</html>
```